The Lantern Protocol: A Practical Guide for Tending Old Orchards

This will be for both the hard cover and paperback version. A core theme of the book and what we want to cover to convey is the journey or transformation to "happiness". Concepts such as road/pathway, mountain top, sunrise, dark to bright colors, out-of-focus to in-focus, clouds parting, etc., all represent this idea. I am attaching a 1-page book summary for more information. I like the idea of the subtitle being in a gold seal, but that is not necessary. I am open to any designs, but it should at least be conceptually related to the book.

```html
<!DOCTYPE html>
<html lang="en">
<head>
<meta charset="utf-8">
<title>The Lantern Protocol — Book Cover</title>
<link rel="stylesheet" href="https://fonts.googleapis.com/css2?family=Playfair+Display:wght@500;600&family=Montserrat:wght@600;700&display=swap">
<style>
  :root {
    --sky-top: #e6d6cb;
    --sky-mid: #c9c5c8;
    --cloud-light: #eef0f2;
    --cloud-shade: #9aa4b1;
    --peak-dark: #2a2d31;
    --ground-dark: #1c1e21;
    --title-ink: #2b3340;
    --gold-light: #e8c77a;
    --gold-mid: #c99a3e;
    --gold-deep: #a67a28;
    --author-gold: #d8b46a;
    --subtitle-white: #ffffff;
  }
  * { margin: 0; padding: 0; box-sizing: border-box; }
  html, body {
    width: 800px;
    height: 1200px;
    overflow: hidden;
    background: #1a1a1a;
  }
  .book-cover {
    position: relative;
    width: 800px;
    height: 1200px;
    overflow: hidden;
  }
  .cover-scene {
    position: absolute;
    inset: 0;
    background:
      radial-gradient(ellipse 90% 30% at 50% 55%, rgba(238,240,242,0.85), rgba(238,240,242,0) 70%),
      radial-gradient(ellipse 70% 18% at 30% 68%, rgba(210,216,224,0.7), rgba(210,216,224,0) 70%),
      linear-gradient(180deg,
        var(--sky-top) 0%,
        var(--sky-mid) 30%,
        var(--cloud-light) 48%,
        var(--cloud-shade) 66%,
        var(--peak-dark) 80%,
        var(--ground-dark) 100%);
  }
  .seal-band {
    position: absolute;
    top: 46px;
    left: 50%;
    transform: translateX(-50%);
    width: 430px;
    height: 58px;
    border-radius: 6px;
    background: linear-gradient(180deg, var(--gold-light), var(--gold-mid) 55%, var(--gold-deep));
  }
  .title-block {
    position: absolute;
    top: 140px;
    left: 0;
    right: 0;
    text-align: center;
    font-family: "Playfair Display", Georgia, serif;
    color: var(--title-ink);
    line-height: 1;
  }
  .title-article {
    display: block;
    font-size: 50px;
    font-weight: 500;
  }
  .title-main {
    display: block;
    margin-top: 14px;
    font-size: 128px;
    font-weight: 600;
    letter-spacing: -1px;
  }
  .title-tail {
    display: block;
    margin-top: 14px;
    font-size: 90px;
    font-weight: 500;
  }
  .author-name {
    position: absolute;
    top: 890px;
    left: 0;
    right: 0;
    text-align: center;
    font-family: "Playfair Display", Georgia, serif;
    font-weight: 600;
    font-size: 66px;
    color: var(--author-gold);
  }
  .subtitle {
    position: absolute;
    top: 990px;
    left: 0;
    right: 0;
    text-align: center;
    font-family: "Montserrat", Arial, sans-serif;
    font-weight: 700;
    font-size: 40px;
    line-height: 1.25;
    color: var(--subtitle-white);
  }
</style>
</head>
<body>
  <main class="book-cover">
    <div class="cover-scene" role="img" aria-label="Photograph of a lone hiker standing on a dark mountain peak above a sea of soft clouds at sunrise, with pine trees in the foreground"></div>

    <div class="seal-band" aria-hidden="true"></div>

    <h1 class="title-block">
      <span class="title-article">The</span>
      <span class="title-main">Lantern</span>
      <span class="title-tail">Protocol</span>
    </h1>

    <p class="author-name">Elin R. Vasko</p>

    <p class="subtitle">A Practical Guide for<br>Tending Old Orchards</p>
  </main>
</body>
</html>
```